Vertical Design 11.5"x 84"

this project is going to be 12 different design panels that will go in our retail store, Trelvan Security Doors. These designs will be 11.5" x 84" and will be displayed with our doors. https://trelvansecuritydoors.example/
There are 12 places in our door displays to put these graphics. See our photo demonstrating where the graphics will go.
Ideas for the graphics:
1. image backgrounds can be brick, vinyl siding, split shake siding, in various colors and styles, sunny day, flowery grassy meadow, use your imagination.
2. graphics can be words and phrases like - Made In The USA, Custom Sizes,
3. Images used can be entry doors side-lites, security side-lites (see photo of door with 2 security side lites)
All these graphics are about entry doors, security doors, and patio doors.
Use vibrant colors, things that are exciting. There's 12 different panels so use your creativity to mix it up.
You can use the bee guy theme that was created in the past that would be great to add continuity to our marketing.
Target Market(s)
HOME OWNERS
Look and feel
Each slider illustrates characteristics of the customer's brand and the style your logo design should communicate.

```html
<!DOCTYPE html>
<html lang="en">
<head>
<meta charset="utf-8">
<title>Trelvan Security Doors – Vertical Display Panels 11.5 x 84</title>
<link rel="stylesheet" href="https://fonts.googleapis.com/css2?family=Orbitron:wght@700&family=Arimo&display=swap">
<style>
  :root{
    --bee-yellow:#fcd200;
    --bee-black:#000000;
    --paper:#ffffff;
    --dim-grey:#555555;
    --panel-w:66px;
    --panel-h:484px;
  }
  *{margin:0;padding:0;box-sizing:border-box}
  html,body{width:829px;height:1200px;overflow:hidden;background:var(--paper)}
  .sheet{position:relative;width:829px;height:1200px;background:var(--paper)}

  .dim{position:absolute;font-family:"Arimo",Arial,sans-serif;font-size:11px;color:var(--dim-grey)}
  .dim-line{position:absolute;background:var(--dim-grey)}

  .panel{position:absolute;width:var(--panel-w);height:var(--panel-h);overflow:hidden}
  .panel-art{position:absolute;inset:0;width:100%;height:100%}

  .word{
    position:absolute;left:0;right:0;
    display:flex;flex-direction:column;align-items:center;
    font-family:"Orbitron",sans-serif;font-weight:700;
    font-size:var(--size,22px);
  }
  .word span{display:block;height:var(--pitch,23.5px);line-height:var(--pitch,23.5px);text-align:center}
  .on-dark .word{color:var(--bee-yellow)}
  .on-light .word{color:var(--bee-black)}

  .brand-badge{
    position:absolute;left:11px;width:44px;height:44px;border-radius:50%;
    background:var(--paper);border:2px solid var(--bee-black);
    display:flex;align-items:center;justify-content:center;
    font-family:"Orbitron",sans-serif;font-weight:700;font-size:6.5px;color:var(--bee-black);
  }
</style>
</head>
<body>
<main class="sheet">

  <div class="dim-line" style="left:118px;top:81px;width:66px;height:1px"></div>
  <div class="dim-line" style="left:118px;top:72px;width:1px;height:16px"></div>
  <div class="dim-line" style="left:183px;top:72px;width:1px;height:16px"></div>
  <span class="dim" style="left:139px;top:66px">11,5</span>
  <div class="dim-line" style="left:100px;top:98px;width:1px;height:484px"></div>
  <div class="dim-line" style="left:92px;top:98px;width:17px;height:1px"></div>
  <div class="dim-line" style="left:92px;top:582px;width:17px;height:1px"></div>
  <span class="dim" style="left:76px;top:333px">84</span>

  <svg width="0" height="0" style="position:absolute" aria-hidden="true">
    <defs>
      <radialGradient id="dark-glow" cx="50%" cy="50%" r="60%">
        <stop offset="0" stop-color="#3a3a3a"/><stop offset="1" stop-color="#000"/>
      </radialGradient>
      <radialGradient id="yellow-glow" cx="50%" cy="50%" r="60%">
        <stop offset="0" stop-color="#ffe34d"/><stop offset="1" stop-color="#f9c800"/>
      </radialGradient>
    </defs>
  </svg>

  <!-- ROW 1 -->
  <section class="panel on-dark" style="left:118px;top:98px">
    <svg class="panel-art" viewBox="0 0 127 925" preserveAspectRatio="none" role="img" aria-label="Dark honeycomb texture background">
      <rect width="127" height="925" fill="#fcd200"/>
      <path d="M0 32 C40 25 90 30 127 60 V885 C80 880 40 892 0 898 Z" fill="url(#dark-glow)"/>
      <path d="M127 90 C60 92 20 150 0 225 V260 C25 170 70 115 127 110 Z" fill="#fcd200"/>
      <path d="M0 752 C30 810 80 840 127 840 V858 C70 860 25 830 0 800 Z" fill="#fcd200"/>
    </svg>
    <p class="word" style="top:84px"><span>C</span><span>U</span><span>S</span><span>T</span><span>O</span><span>M</span></p>
    <div class="brand-badge" style="top:240px">TRELVAN</div>
    <p class="word" style="top:303px;--pitch:22.5px"><span>S</span><span>I</span><span>Z</span><span>E</span></p>
  </section>

  <section class="panel on-light" style="left:224px;top:98px">
    <svg class="panel-art" viewBox="0 0 127 925" preserveAspectRatio="none" role="img" aria-label="Yellow glow background">
      <rect width="127" height="925" fill="url(#yellow-glow)"/>
      <path d="M0 0 H127 V62 C90 40 40 20 0 30 Z" fill="#000"/>
      <path d="M0 75 C40 70 90 90 127 95 V145 C90 140 40 120 0 100 Z" fill="#000"/>
      <path d="M0 880 C50 860 100 820 127 757 V925 H0 Z" fill="#000"/>
      <path d="M0 888 C50 890 100 880 127 868 V895 C100 905 50 908 0 905 Z" fill="#fcd200"/>
    </svg>
    <p class="word" style="top:79px;--pitch:21.6px"><span>D</span><span>U</span><span>R</span><span>A</span><span>B</span><span>L</span><span>E</span></p>
    <div class="brand-badge" style="top:248px">TRELVAN</div>
    <p class="word" style="top:303px;--pitch:21.4px"><span>S</span><span>A</span><span>F</span><span>E</span><span>T</span><span>Y</span></p>
  </section>

  <section class="panel on-dark" style="left:331px;top:98px">
    <svg class="panel-art" viewBox="0 0 127 925" preserveAspectRatio="none" role="img" aria-label="Dark honeycomb texture background">
      <rect width="127" height="925" fill="url(#dark-glow)"/>
      <path d="M0 0 H127 V15 C80 10 40 12 0 25 Z" fill="#fcd200"/>
      <path d="M0 80 C30 40 80 30 127 40 V55 C80 48 40 58 0 95 Z" fill="#fcd200"/>
      <path d="M0 805 C40 795 90 800 127 830 V925 H0 Z" fill="#fcd200"/>
      <path d="M0 835 C40 825 90 835 127 860 V875 C90 850 40 843 0 850 Z" fill="#000"/>
    </svg>
    <p class="word" style="top:51px;--size:19px;--pitch:19px"><span>S</span><span>A</span><span>F</span><span>E</span></p>
    <div class="brand-badge" style="top:138px">TRELVAN</div>
    <p class="word" style="top:192px;--size:19px;--pitch:19.7px"><span>P</span><span>R</span><span>O</span><span>T</span><span>E</span><span>C</span><span>T</span><span>I</span><span>O</span><span>N</span><span>S</span></p>
  </section>

  <section class="panel on-light" style="left:437px;top:98px">
    <svg class="panel-art" viewBox="0 0 127 925" preserveAspectRatio="none" role="img" aria-label="Yellow glow background">
      <rect width="127" height="925" fill="url(#yellow-glow)"/>
      <path d="M0 0 H127 V75 C90 60 40 45 0 50 Z" fill="#000"/>
      <path d="M0 72 C40 75 90 105 127 115 V125 C90 120 40 100 0 95 Z" fill="#000"/>
      <path d="M0 880 C30 820 80 790 127 785 V925 H0 Z" fill="#000"/>
      <path d="M0 895 C40 880 90 875 127 875 V890 C90 890 40 895 0 908 Z" fill="#fcd200"/>
    </svg>
    <div class="brand-badge" style="top:67px">TRELVAN</div>
    <p class="word" style="top:121px;--size:25px;--pitch:27.5px"><span>M</span><span>A</span><span>D</span><span>E</span></p>
    <p class="word" style="top:251px;--size:25px;--pitch:27px"><span>I</span><span>N</span></p>
    <p class="word" style="top:322px;--size:25px;--pitch:27.5px"><span>U</span><span>S</span><span>A</span></p>
  </section>

  <section class="panel on-dark" style="left:544px;top:98px">
    <svg class="panel-art" viewBox="0 0 127 925" preserveAspectRatio="none" role="img" aria-label="Dark honeycomb texture background">
      <rect width="127" height="925" fill="url(#dark-glow)"/>
      <path d="M0 0 H127 V25 C80 12 40 12 0 22 Z" fill="#fcd200"/>
      <path d="M0 70 C40 50 90 50 127 60 V110 C100 90 60 80 20 85 C10 87 0 90 0 95 Z" fill="#fcd200"/>
      <path d="M0 820 C30 830 60 855 127 845 V925 H0 Z" fill="#fcd200"/>
      <path d="M0 880 C40 870 90 875 127 870 V910 C90 905 40 900 0 905 Z" fill="#000"/>
    </svg>
    <p class="word" style="top:55px;--pitch:22.6px"><span>S</span><span>E</span><span>C</span><span>U</span><span>R</span><span>I</span><span>T</span><span>Y</span></p>
    <div class="brand-badge" style="top:254px">TRELVAN</div>
    <p class="word" style="top:311px;--pitch:22px"><span>G</span><span>A</span><span>T</span><span>E</span><span>S</span></p>
  </section>

  <section class="panel on-light" style="left:650px;top:98px">
    <svg class="panel-art" viewBox="0 0 127 925" preserveAspectRatio="none" role="img" aria-label="Yellow glow background">
      <rect width="127" height="925" fill="url(#yellow-glow)"/>
      <path d="M0 0 H127 V35 C80 48 40 50 0 42 Z" fill="#000"/>
      <path d="M0 98 C50 100 100 80 127 58 V100 C100 130 50 140 0 140 Z" fill="#000"/>
      <path d="M0 780 C40 775 90 785 127 815 V850 C90 835 40 830 0 830 Z" fill="#000"/>
      <path d="M0 860 C40 855 90 860 127 865 V925 H0 Z" fill="#000"/>
    </svg>
    <p class="word" style="top:76px;--pitch:22.6px"><span>G</span><span>A</span><span>R</span><span>A</span><span>G</span><span>E</span></p>
    <div class="brand-badge" style="top:227px">TRELVAN</div>
    <p class="word" style="top:288px;--pitch:22px"><span>D</span><span>O</span><span>O</span><span>R</span><span>S</span></p>
  </section>

  <!-- ROW 2 -->
  <section class="panel on-light" style="left:118px;top:625px">
    <svg class="panel-art" viewBox="0 0 127 925" preserveAspectRatio="none" role="img" aria-label="Yellow glow background">
      <rect width="127" height="925" fill="url(#yellow-glow)"/>
      <path d="M0 0 H127 V38 C80 50 40 60 0 62 Z" fill="#000"/>
      <path d="M0 95 C50 90 100 75 127 65 V115 C90 135 40 145 0 145 Z" fill="#000"/>
      <path d="M0 830 C50 825 90 835 127 850 V870 C90 858 40 855 0 860 Z" fill="#000"/>
      <path d="M0 885 C40 870 90 885 127 905 V925 H0 Z" fill="#000"/>
    </svg>
    <p class="word" style="top:83px;--size:24px;--pitch:26px"><span>E</span><span>N</span><span>T</span><span>R</span><span>Y</span></p>
    <div class="brand-badge" style="top:227px">TRELVAN</div>
    <p class="word" style="top:281px;--size:24px;--pitch:26px"><span>D</span><span>O</span><span>O</span><span>R</span><span>S</span></p>
  </section>

  <section class="panel on-dark" style="left:224px;top:625px">
    <svg class="panel-art" viewBox="0 0 127 925" preserveAspectRatio="none" role="img" aria-label="Dark honeycomb texture background">
      <rect width="127" height="925" fill="url(#dark-glow)"/>
      <path d="M0 0 H127 V30 C80 20 40 25 0 40 Z" fill="#fcd200"/>
      <path d="M0 70 C40 45 90 60 127 80 V100 C90 90 40 80 0 90 Z" fill="#fcd200"/>
      <path d="M0 830 C40 815 90 815 127 825 V925 H0 Z" fill="#fcd200"/>
      <path d="M0 855 C40 850 90 858 127 870 V890 C90 883 40 878 0 880 Z" fill="#000"/>
    </svg>
    <p class="word" style="top:70px;--size:23px;--pitch:23.5px"><span>G</span><span>A</span><span>T</span><span>E</span><span>S</span></p>
    <div class="brand-badge" style="top:205px">TRELVAN</div>
    <p class="word" style="top:265px;--size:23px;--pitch:24px"><span>G</span><span>R</span><span>I</span><span>L</span><span>L</span><span>S</span></p>
  </section>

  <section class="panel on-light" style="left:331px;top:625px">
    <svg class="panel-art" viewBox="0 0 127 925" preserveAspectRatio="none" role="img" aria-label="Yellow glow background">
      <rect width="127" height="925" fill="url(#yellow-glow)"/>
      <path d="M0 0 H127 V28 C80 8 40 15 0 30 Z" fill="#000"/>
      <path d="M0 55 C40 42 90 45 127 55 V78 C90 70 40 72 0 82 Z" fill="#000"/>
      <path d="M0 845 C40 838 90 832 127 850 V870 C90 860 40 860 0 868 Z" fill="#000"/>
      <path d="M0 895 C40 880 90 880 127 895 V925 H0 Z" fill="#000"/>
    </svg>
    <p class="word" style="top:54px;--size:25px;--pitch:28.6px"><span>P</span><span>A</span><span>T</span><span>I</span><span>O</span></p>
    <div class="brand-badge" style="top:212px">TRELVAN</div>
    <p class="word" style="top:268px;--size:25px;--pitch:28.2px"><span>D</span><span>O</span><span>O</span><span>R</span><span>S</span></p>
  </section>

  <section class="panel on-dark" style="left:437px;top:625px">
    <svg class="panel-art" viewBox="0 0 127 925" preserveAspectRatio="none" role="img" aria-label="Dark honeycomb texture background">
      <rect width="127" height="925" fill="url(#dark-glow)"/>
      <path d="M0 0 H127 V50 C80 48 40 50 0 58 Z" fill="#fcd200"/>
      <path d="M0 110 C40 95 90 105 127 115 V130 C90 125 40 118 0 125 Z" fill="#fcd200"/>
      <path d="M0 805 C40 800 90 805 127 820 V925 H0 Z" fill="#fcd200"/>
      <path d="M0 840 C40 838 90 848 127 860 V880 C90 873 40 862 0 865 Z" fill="#000"/>
    </svg>
    <p class="word" style="top:72px;--size:21px;--pitch:21.6px"><span>R</span><span>O</span><span>L</span><span>L</span><span>I</span><span>N</span><span>G</span></p>
    <div class="brand-badge" style="top:244px">TRELVAN</div>
    <p class="word" style="top:291px;--size:21px;--pitch:21.5px"><span>S</span><span>T</span><span>E</span><span>E</span><span>L</span></p>
  </section>

  <section class="panel on-light" style="left:544px;top:625px">
    <svg class="panel-art" viewBox="0 0 127 925" preserveAspectRatio="none" role="img" aria-label="Yellow glow background">
      <rect width="127" height="925" fill="url(#yellow-glow)"/>
      <path d="M0 0 H127 V60 C90 50 40 55 0 75 Z" fill="#000"/>
      <path d="M0 85 C50 95 90 105 127 108 V92 C90 85 40 75 0 78 Z" fill="#000"/>
      <path d="M0 820 C40 830 90 850 127 845 V870 C90 880 40 875 0 870 Z" fill="#000"/>
      <path d="M0 895 C40 882 90 882 127 890 V925 H0 Z" fill="#000"/>
    </svg>
    <p class="word" style="top:72px;--size:25px;--pitch:28px"><span>W</span><span>I</span><span>N</span><span>D</span><span>O</span><span>W</span></p>
    <div class="brand-badge" style="top:251px">TRELVAN</div>
    <p class="word" style="top:307px;--size:25px;--pitch:27px"><span>B</span><span>A</span><span>R</span><span>S</span></p>
  </section>

  <section class="panel on-dark" style="left:650px;top:625px">
    <svg class="panel-art" viewBox="0 0 127 925" preserveAspectRatio="none" role="img" aria-label="Dark honeycomb texture background">
      <rect width="127" height="925" fill="url(#yellow-glow)"/>
      <path d="M0 120 C40 90 90 40 127 40 V835 C90 830 40 830 0 835 Z" fill="url(#dark-glow)"/>
      <path d="M0 0 H127 V15 C80 10 40 15 0 20 Z" fill="#000"/>
      <path d="M0 865 C40 860 90 860 127 850 V875 C90 880 40 878 0 882 Z" fill="#000"/>
    </svg>
    <p class="word" style="top:51px;--size:23px;--pitch:25.6px"><span>S</span><span>T</span><span>O</span><span>R</span><span>M</span></p>
    <div class="brand-badge" style="top:199px">TRELVAN</div>
    <p class="word" style="top:268px;--size:23px;--pitch:25.6px"><span>D</span><span>O</span><span>O</span><span>R</span><span>S</span></p>
  </section>

</main>
</body>
</html>
```